Handmade clothes, homewares and fashion accessories

I need a business card for my new company that crochets, knits and sews homewares, fashion accessories and clothing. I would like a soft cream coloured background (maybe, or a colour scheme that you would think would compliment the graphics) with a funky designed robin sitting down with her feet forward and gently tangled up with a ball of wool and a bobbin of cotton, one either side of her. I would like the robin to have the classic red breast and to be looking happy.
Updates
Hi everyone
Sorry to be a pain, but I think I would like the design to be unisex as my previous one was too female orientated. Thanks

Hi everyone
I am leaning more towards a teal colour scheme with the robin being the feature and a more neutral font, not so feminine. Thanks

Target Market(s)
Females of all ages
Industry/Entity Type
Fashion
Contact Information for Business Card
Velvet Heron
Handmade in Larkfield Southern Vale
Moira Fenwick PO Box 317 Larkfield SV 6418
Look and feel
Each slider illustrates characteristics of the customer's brand and the style your logo design should communicate.

```html
<!DOCTYPE html>
<html lang="en">
<head>
<meta charset="utf-8">
<title>Velvet Heron – Business Card</title>
<link rel="stylesheet" href="https://fonts.googleapis.com/css2?family=Stardos+Stencil:wght@700&family=Tinos:wght@700&display=swap">
<style>
  :root {
    --teal: #1f9a90;
    --teal-deep: #17857c;
    --paper: #ffffff;
    --ink: #2a2a2a;
    --robin-red: #e8281e;
    --edge: #2aa79c;
  }
  html, body {
    margin: 0;
    padding: 0;
    overflow: hidden;
    background: var(--paper);
  }
  .card {
    position: relative;
    width: 1200px;
    height: 705px;
    background: var(--paper);
    overflow: hidden;
  }
  .card__frame {
    position: absolute;
    left: 664px;
    top: 0;
    width: 532px;
    height: 703px;
    border-top: 2px solid var(--edge);
    border-right: 2px solid var(--edge);
    border-bottom: 2px solid var(--edge);
  }
  .card__knit-panel {
    position: absolute;
    left: 0;
    top: 26px;
    width: 679px;
    height: 677px;
    background: linear-gradient(160deg, var(--teal) 0%, var(--teal-deep) 100%);
  }
  .card__phone {
    position: absolute;
    right: 10px;
    top: 36px;
    margin: 0;
    font-family: "Tinos", "Times New Roman", serif;
    font-weight: 700;
    font-size: 27px;
    color: var(--ink);
    letter-spacing: 0.5px;
  }
  .brand__mark {
    position: absolute;
    left: 850px;
    top: 160px;
    width: 120px;
    height: 120px;
  }
  .brand__name {
    position: absolute;
    left: 0;
    top: 314px;
    width: 1200px;
    margin: 0;
    padding-left: 170px;
    box-sizing: border-box;
    font-family: "Stardos Stencil", "Arial Black", sans-serif;
    font-weight: 700;
    font-size: 96px;
    line-height: 1;
    letter-spacing: 4px;
    white-space: nowrap;
    background: linear-gradient(90deg, var(--paper) 0, var(--paper) 679px, var(--ink) 679px, var(--ink) 100%);
    -webkit-background-clip: text;
    background-clip: text;
    color: transparent;
  }
  .brand__rule {
    position: absolute;
    top: 414px;
    height: 3px;
  }
  .brand__rule--left { left: 170px; width: 492px; background: var(--paper); }
  .brand__rule--right { left: 688px; width: 372px; background: var(--ink); }
  .brand__tagline {
    position: absolute;
    left: 874px;
    top: 420px;
    margin: 0;
    font-family: "Stardos Stencil", "Arial Black", sans-serif;
    font-weight: 700;
    font-size: 31px;
    color: var(--robin-red);
    letter-spacing: 1px;
  }
  .card__address {
    position: absolute;
    left: 13px;
    top: 656px;
    width: 1176px;
    margin: 0;
    font-family: "Tinos", "Times New Roman", serif;
    font-weight: 700;
    font-size: 22px;
    letter-spacing: 0.6px;
    white-space: nowrap;
    text-align: justify;
    text-align-last: justify;
    background: linear-gradient(90deg, var(--paper) 0, var(--paper) 666px, var(--ink) 666px, var(--ink) 100%);
    -webkit-background-clip: text;
    background-clip: text;
    color: transparent;
  }
</style>
</head>
<body>
  <main class="card">
    <div class="card__frame"></div>
    <div class="card__knit-panel" role="img" aria-label="Teal knitted wool texture"></div>

    <p class="card__phone">TEL:0412 386 294</p>

    <svg class="brand__mark" viewBox="0 0 120 120" aria-hidden="true">
      <circle cx="60" cy="60" r="56" fill="var(--robin-red)"/>
    </svg>

    <h1 class="brand__name">VELVET HERON</h1>
    <div class="brand__rule brand__rule--left"></div>
    <div class="brand__rule brand__rule--right"></div>
    <p class="brand__tagline">HANDMADE</p>

    <p class="card__address">ADD: LARKFIELD ,SOUTHERN VALE, MOIRA FENWICK PO BOX 317 LARKFIELD SV 6418</p>
  </main>
</body>
</html>
```